Solar Billboard Design

We require a billboard 24ftx10ft in size for our solar company.
Artwork Requirement’s:
• Sent on PDF file
• At least 300 dpi
• Scaled to 25% of banner size (24ft x 10ft)
• Please allow at least 40mm space from the artwork edge to allow for any hems and eyelets. This will ensure any important text/images are not cropped/overlapped.
The billboard must have on it:
Solar & Battery Packages
From £8750
In Stock Now!
brightfieldpower.co.uk (must stand out)
________________________
I have attached our logo and some images. I'm not sure if they are good enough quality so you may need to use a stock image.
Kind regards,
Marcus
Target Market(s)
Men & Women aged 35-70, homeowners
Industry/Entity Type
Solar / Construction
Look and feel
Each slider illustrates characteristics of the customer's brand and the style your logo design should communicate.

```html
<!DOCTYPE html>
<html lang="en">
<head>
<meta charset="utf-8">
<title>Brightfield Energy Group – Solar &amp; Battery Billboard</title>
<link href="https://fonts.googleapis.com/css2?family=Montserrat:wght@400;500;700&display=swap" rel="stylesheet">
<style>
  :root {
    --surround: #4a4849;
    --paper: #ffffff;
    --brand-green: #4aba67;
    --ink: #444042;
    --roof: #e0824a;
    --panel: #1f2f6b;
  }
  * { margin: 0; padding: 0; box-sizing: border-box; }
  html, body { width: 1200px; height: 600px; overflow: hidden; background: var(--surround); }
  .billboard {
    position: relative;
    width: 1200px; height: 600px;
    background: var(--surround);
    font-family: "Montserrat", sans-serif;
    color: var(--ink);
  }
  .artboard {
    position: absolute;
    left: 54px; top: 71px;
    width: 1081px; height: 452px;
    background: var(--paper);
    overflow: hidden;
  }
  .shapes { position: absolute; inset: 0; }
  .brand {
    position: absolute;
    left: 38px; top: 30px;
    display: flex; align-items: center; gap: 18px;
  }
  .brand-square {
    width: 62px; height: 62px;
    background: var(--brand-green);
  }
  .brand-name {
    font-weight: 500;
    font-size: 22px;
    line-height: 32px;
    letter-spacing: 0.16em;
    color: var(--ink);
    text-transform: uppercase;
  }
  .web-address {
    position: absolute;
    right: 19px; top: 36px;
    font-weight: 700;
    font-size: 38px;
    letter-spacing: 0.1em;
    color: var(--paper);
    white-space: nowrap;
  }
  .headline {
    position: absolute;
    left: 31px; top: 170px;
    font-weight: 700;
    font-size: 54px;
    line-height: 66px;
    letter-spacing: -0.01em;
    text-transform: uppercase;
    color: var(--ink);
  }
  .price {
    position: absolute;
    left: 36px; top: 370px;
    color: var(--paper);
    font-size: 52px;
    white-space: nowrap;
  }
  .price-from { font-weight: 400; margin-right: 10px; }
  .price-amount { font-weight: 700; letter-spacing: -0.01em; }
  .stock-note {
    position: absolute;
    left: 360px; top: 355px;
    width: 170px;
    text-align: center;
    font-weight: 700;
    font-size: 38px;
    line-height: 42px;
    color: var(--ink);
  }
</style>
</head>
<body>
  <main class="billboard">
    <section class="artboard">
      <svg class="shapes" width="1081" height="452" viewBox="0 0 1081 452" aria-hidden="false">
        <defs>
          <linearGradient id="roofPanels" x1="0" y1="0" x2="1" y2="1">
            <stop offset="0" stop-color="var(--roof)"/>
            <stop offset="0.2" stop-color="#2a3a78"/>
            <stop offset="0.8" stop-color="var(--panel)"/>
            <stop offset="1" stop-color="var(--roof)"/>
          </linearGradient>
        </defs>
        <polygon class="web-band" points="425,0 1081,0 1081,104 463,104" fill="var(--brand-green)"/>
        <polygon class="price-band" points="0,348 331,348 369,452 0,452" fill="var(--brand-green)"/>
        <polygon class="roof-photo" role="img" aria-label="Photo of blue solar panels mounted on an orange tiled roof"
                 points="635,104 1081,104 1081,452 520,452" fill="url(#roofPanels)"/>
      </svg>

      <div class="brand">
        <span class="brand-square"></span>
        <p class="brand-name">Brightfield<br>Energy<br>Group</p>
      </div>

      <p class="web-address">brightfieldpower.co.uk</p>

      <h1 class="headline">Solar &amp; Battery<br>Packages</h1>

      <p class="price"><span class="price-from">from</span><span class="price-amount">£8750</span></p>

      <p class="stock-note">In Stock Now!</p>
    </section>
  </main>
</body>
</html>
```